Natural Cosmetics need a Packaging Design

We need a PACKAGING design for labels on hand/body wash bottles and soap paper boxes.
We target at high end markets.
We expect a contemporary and trendy design.
We don't need a separate logo. The brand name "Va Mirel" acts as the logo.
We want a modern and classic font for "Va Mirel".
Please see attached pictures for packaging samples.

Industry/Entity Type

Cosmetics

Requirements
Should not have
• a separate logo from the brand name

```html
<!DOCTYPE html>
<html lang="en">
<head>
<meta charset="utf-8">
<title>Va Mirel Body Wash Label</title>
<link rel="stylesheet" href="https://fonts.googleapis.com/css2?family=Poiret+One&family=Josefin+Sans:wght@300;400&display=swap">
<style>
  :root {
    --label-white: #f7f7f7;
    --label-shade: #e6e6e6;
    --ink-dark: #2b2b2b;
    --ink-body: #555555;
    --bar-dark: #3a3a3a;
    --bar-text: #f2f2f2;
    --wave-tone: #dcdcdc;
  }
  html, body {
    margin: 0;
    padding: 0;
    width: 1078px;
    height: 1200px;
    overflow: hidden;
    background: var(--label-white);
  }
  .label {
    position: relative;
    width: 1078px;
    height: 1200px;
    background: linear-gradient(90deg, var(--label-shade) 0%, var(--label-white) 30%, var(--label-white) 70%, var(--label-shade) 100%);
    overflow: hidden;
  }
  .wave-texture {
    position: absolute;
    left: 0;
    top: 620px;
    width: 1078px;
    height: 580px;
  }
  .brand-name {
    position: absolute;
    top: 190px;
    left: 0;
    width: 1078px;
    text-align: center;
    margin: 0;
    font-family: "Poiret One", sans-serif;
    font-weight: 400;
    font-size: 170px;
    letter-spacing: 4px;
    color: var(--ink-dark);
  }
  .product-block {
    position: absolute;
    top: 560px;
    right: 120px;
    width: 700px;
    text-align: left;
  }
  .product-type {
    margin: 0;
    font-family: "Poiret One", sans-serif;
    font-size: 118px;
    line-height: 1;
    color: var(--ink-dark);
    text-align: right;
    letter-spacing: 1px;
  }
  .product-variant {
    margin: 14px 0 0;
    padding: 6px 18px 2px;
    background: var(--bar-dark);
    color: var(--bar-text);
    font-family: "Josefin Sans", sans-serif;
    font-weight: 400;
    font-size: 70px;
    line-height: 1.15;
    text-align: right;
  }
  .product-description {
    margin: 18px 0 0;
    font-family: "Josefin Sans", sans-serif;
    font-weight: 300;
    font-size: 40px;
    line-height: 1.3;
    color: var(--ink-body);
  }
  .volume {
    position: absolute;
    bottom: 80px;
    left: 0;
    width: 1078px;
    text-align: center;
    margin: 0;
    font-family: "Josefin Sans", sans-serif;
    font-weight: 300;
    font-size: 44px;
    color: var(--ink-body);
  }
</style>
</head>
<body>
  <main class="label">
    <svg class="wave-texture" role="img" aria-label="Fine flowing line pattern sweeping across the lower label" viewBox="0 0 1078 580" preserveAspectRatio="none">
      <defs>
        <radialGradient id="waveGlow" cx="25%" cy="60%" r="70%">
          <stop offset="0%" stop-color="var(--wave-tone)" stop-opacity="0.9"/>
          <stop offset="100%" stop-color="var(--wave-tone)" stop-opacity="0"/>
        </radialGradient>
      </defs>
      <rect width="1078" height="580" fill="url(#waveGlow)"/>
    </svg>

    <h1 class="brand-name">Va Mirel</h1>

    <section class="product-block">
      <h2 class="product-type">BODY WASH</h2>
      <p class="product-variant">Moisturizer Smooth</p>
      <p class="product-description">Lorem Ipsum is simply dummy text of the printing and typesetting industry body wash</p>
    </section>

    <p class="volume">16 Fl. Oz (473 ml)</p>
  </main>
</body>
</html>
```